Business Cards Design for the electrical wholesaler: clean bold dynamic :)

We need a business card design that would follow our latest brand guidelines. As an electrical wholesaler we want to bring a fresh look and feel into the industry. The design should be clean bold and dynamic. It should come alive with the renewed energy of our green colour. Our grey colour should keep things balanced and complement the notion of maturity and responsibility. We employ Lato as a corporate font however are not bound by this font and we’re open to interpretation here.

Target Market(s)

Electrical contractors

Industry/Entity Type

Business

Contact Information for Business Card

Logo
Name & Surname: Olesia Hrybenko
Job Title: Director of Marketing
Email: olesia.hrybenko@mailvex.com
Cell phone: XXX.XXX.XXXX
Address: 20517 - 88 Ave. Edmonton, AB, Canada. T6K 2N8
Business Phone: 780.362.7048
Website: www.kopra.ca

Font styles to use
Other font styles liked:
• Lato

Requirements
Must have
• Logo & website
Nice to have
• Brand elements - some of them you may find in the attached Brand Guidelines (e.g. three lines on the background signifying "W")

```html
<!DOCTYPE html>
<html lang="en">
<head>
<meta charset="utf-8">
<title>kopra business cards</title>
<link rel="stylesheet" href="https://fonts.googleapis.com/css2?family=Roboto:wght@300;400;500;700&display=swap">
<style>
  :root {
    --stage: #e9e7e3;
    --card-white: #ffffff;
    --card-dark: #1d1d1e;
    --card-dark-edge: #2a2a2b;
    --brand-green: #7cc61c;
    --brand-grey: #3d3f42;
    --text-grey: #4a4b4d;
    --rule: #2e2e30;
    --band: #f1f1f1;
  }
  * { margin: 0; padding: 0; box-sizing: border-box; }
  html, body {
    width: 1200px; height: 800px; overflow: hidden;
    background: var(--stage);
    font-family: "Roboto", Arial, sans-serif;
  }
  .sheet {
    width: 1200px; height: 800px;
    display: flex; align-items: center; justify-content: center; gap: 40px;
  }
  .card {
    position: relative; width: 560px; height: 320px; overflow: hidden;
    box-shadow: 0 10px 28px rgba(0,0,0,0.18);
  }

  /* front */
  .card--front { background: var(--card-white); }
  .card__bands { position: absolute; inset: 0; }
  .brand {
    position: absolute; display: flex; align-items: center; gap: 12px;
  }
  .brand__mark { width: 30px; height: 30px; background: var(--brand-green); }
  .brand__name { font-weight: 500; letter-spacing: 0.5px; }
  .card--front .brand { left: 48px; top: 52px; }
  .card--front .brand__name { font-size: 44px; color: var(--brand-grey); }

  .person { position: absolute; left: 48px; top: 148px; }
  .person__name { font-size: 22px; font-weight: 300; color: var(--text-grey); }
  .person__title { font-size: 12.5px; font-weight: 700; color: #222; margin-top: 2px; }

  .rule-long {
    position: absolute; left: 48px; right: 0; top: 194px;
    height: 1px; background: var(--rule);
  }
  .address {
    position: absolute; right: 36px; top: 150px; text-align: right;
    font-size: 12px; line-height: 1.35; color: #222;
  }
  .rule-short {
    position: absolute; left: 48px; top: 224px; width: 140px;
    height: 1px; background: var(--rule);
  }
  .contacts {
    position: absolute; left: 48px; top: 234px; list-style: none;
    font-size: 12.5px; color: #333; line-height: 1.55;
  }
  .contacts li { display: flex; align-items: center; gap: 8px; }
  .contacts svg { width: 10px; height: 10px; flex: none; }

  /* back */
  .card--back {
    background: linear-gradient(135deg, var(--card-dark-edge), var(--card-dark) 55%, #161617);
  }
  .card--back .brand { left: 50%; top: 118px; transform: translateX(-50%); gap: 16px; }
  .card--back .brand__mark { width: 38px; height: 38px; }
  .card--back .brand__name { font-size: 56px; color: #fff; }
  .back-web {
    position: absolute; left: 0; right: 0; top: 236px; text-align: center;
    font-size: 13px; letter-spacing: 5px; color: var(--brand-green);
  }
</style>
</head>
<body>
<main class="sheet">
  <section class="card card--front" aria-label="Business card front">
    <svg class="card__bands" viewBox="0 0 560 320" aria-hidden="true">
      <path d="M300 0 C360 60 400 140 430 320 L470 320 C440 140 400 60 350 0 Z" fill="var(--band)"/>
      <path d="M370 0 C430 60 470 140 500 320 L540 320 C510 140 470 60 420 0 Z" fill="var(--band)"/>
      <path d="M440 0 C500 60 540 140 560 260 L560 130 C540 70 520 30 490 0 Z" fill="var(--band)"/>
    </svg>

    <div class="brand">
      <span class="brand__mark"></span>
      <span class="brand__name">kopra</span>
    </div>

    <div class="address">20517 - 88 Ave. Edmonton, AB<br>T6K 2N8</div>

    <div class="person">
      <p class="person__name">Olesia Hrybenko</p>
      <p class="person__title">Manager Finance</p>
    </div>
    <div class="rule-long"></div>
    <div class="rule-short"></div>

    <ul class="contacts">
      <li>
        <svg viewBox="0 0 10 10"><rect x="2.5" y="0.5" width="5" height="9" rx="1" fill="none" stroke="var(--brand-green)" stroke-width="1.2"/></svg>
        780.362.7048
      </li>
      <li>
        <svg viewBox="0 0 10 10"><rect x="0.5" y="2" width="9" height="6" fill="none" stroke="var(--brand-green)" stroke-width="1.2"/><path d="M0.5 2 L5 5.5 L9.5 2" fill="none" stroke="var(--brand-green)" stroke-width="1.2"/></svg>
        hello@kopra.ca
      </li>
      <li>
        <svg viewBox="0 0 10 10"><circle cx="5" cy="5" r="4.4" fill="none" stroke="var(--brand-green)" stroke-width="1.2"/><path d="M0.6 5 H9.4 M5 0.6 C2.5 3 2.5 7 5 9.4 M5 0.6 C7.5 3 7.5 7 5 9.4" fill="none" stroke="var(--brand-green)" stroke-width="0.9"/></svg>
        www.kopra.ca
      </li>
    </ul>
  </section>

  <section class="card card--back" aria-label="Business card back">
    <div class="brand">
      <span class="brand__mark"></span>
      <span class="brand__name">kopra</span>
    </div>
    <p class="back-web">www.kopra.ca</p>
  </section>
</main>
</body>
</html>
```